2024 Veltmore Financial Team Deck

I have created a power point slide deck and I need the slide deck recreated. Organized, with better color, background pictures, etc. I am thinking the colors for the presentation can be navy blue, and white, and gold, with hints of silver and black. We are financial planning firm that specializes in working with tech companies in silicon valley.

```html
<!DOCTYPE html>
<html lang="en">
<head>
<meta charset="utf-8">
<title>Veltmore Financial 2024 Team Deck</title>
<link href="https://fonts.googleapis.com/css2?family=Montserrat:wght@400;500;600;700&family=Roboto:wght@300;400;500;700;900&display=swap" rel="stylesheet">
<style>
:root{
  --navy:#0d1a4f;
  --navy-deep:#08123a;
  --gold:#d9b65b;
  --gold-dark:#b8913a;
  --ink:#1b2356;
  --text:#3a3f5c;
  --silver:#c4c8cf;
  --bg:#e3e4e7;
  --white:#ffffff;
}
*{box-sizing:border-box;margin:0;padding:0}
html,body{width:1056px;height:1200px;overflow:hidden;background:var(--bg)}
.canvas{position:relative;width:1056px;height:1200px;background:linear-gradient(135deg,#e8e9ec,#dcdde1);font-family:"Montserrat",sans-serif;color:var(--ink)}
.slide{position:absolute;width:322px;height:181px;background:var(--white);overflow:hidden;box-shadow:0 2px 5px rgba(0,0,0,.28)}
.slide > *{position:absolute}
.navy{background:var(--navy)}
.sq{width:9px;height:9px;background:linear-gradient(135deg,#e8ca78,var(--gold-dark));top:8px;right:11px}
.sq.left{left:7px;right:auto}
.title{left:10px;top:9px;font:700 13px/1 "Roboto",sans-serif;color:var(--ink)}
.bar{left:10px;top:29px;width:37px;height:3px;background:var(--gold)}
.foot{left:15px;right:14px;bottom:8px;display:flex;align-items:center;gap:3px;font:500 4.6px "Montserrat",sans-serif;letter-spacing:1.9px;color:var(--gold)}
.foot .rule{flex:1;height:.6px;background:var(--gold)}
.foot .pg{position:relative;width:6px;height:6px;display:grid;place-items:center;font:700 2.6px "Roboto",sans-serif;letter-spacing:0;color:var(--navy);isolation:isolate}
.foot .pg::before{content:"";position:absolute;inset:.9px;background:var(--gold);transform:rotate(45deg);z-index:-1}
.foot.on-navy span{color:var(--white)}
.photo{display:block}

/* cover */
.cover-title{left:187px;top:56px;font-family:"Roboto",sans-serif;line-height:24px}
.cover-title .l1{display:block;font-weight:400;font-size:19px;color:var(--white);letter-spacing:.4px}
.cover-title .l2{display:block;font-weight:900;font-size:20px;color:var(--gold)}
.cover-title .l3{display:block;font-weight:500;font-size:19px;color:var(--white)}
.cover-web{left:187px;top:158px;width:118px;display:flex;align-items:center;gap:2px;font:500 4.6px "Montserrat",sans-serif;letter-spacing:1.9px;color:var(--gold)}
.cover-web i{flex:1;height:.6px;background:var(--white)}

/* side panels */
.side-panel{left:0;top:0;width:104px;height:181px;background:var(--navy)}
.panel-head{left:15px;top:27px;font:700 13.5px/15px "Roboto",sans-serif;color:var(--gold)}
.panel-copy{left:15px;top:73px;width:82px;font:400 7.4px/9.6px "Montserrat",sans-serif;color:var(--white)}
.copy-block{left:128px;width:172px;font:400 4.2px/6.2px "Montserrat",sans-serif;color:var(--text)}
.copy-block h4{font:600 5.4px/8px "Montserrat",sans-serif;color:var(--navy)}
.copy-block ul{list-style:none}
.copy-block li{position:relative;padding-left:8px;margin-top:3.2px}
.copy-block li::before{content:"•";position:absolute;left:1px}

/* vision & recap small copy */
.fine{left:14px;right:12px;top:38px;font:400 3.2px/4.3px "Montserrat",sans-serif;color:var(--text)}
.fine li{margin-bottom:3.4px;list-style:disc;margin-left:4px}
.vision-date{font:600 5.5px "Roboto",sans-serif;margin-left:3px}
.recap{left:10px;right:12px;top:32px;font:400 2.7px/3.6px "Montserrat",sans-serif;color:var(--text)}
.recap p{margin-bottom:3px}

/* org charts */
.org-box{height:27px;width:60px;border:2px solid var(--navy);border-radius:2px;display:grid;place-items:center;font:700 8.5px "Roboto",sans-serif}
.org-box.lead{background:var(--gold);color:var(--navy)}
.org-box.member{background:var(--navy);color:var(--white);border-color:var(--gold)}
.org-name{font:700 4.4px/1.3 "Montserrat",sans-serif;color:var(--navy)}
.org-role{display:block;font:400 3.2px/1.3 "Montserrat",sans-serif;color:#7a7f95}

/* section divider */
.divider-text{left:0;right:0;top:70px;text-align:center;font:900 16px/1 "Roboto",sans-serif;color:var(--white);letter-spacing:.3px}
.divider-frame{left:58px;top:97px;width:206px;height:13px;border:1px solid var(--gold);border-top:none}
.divider-frame::before,.divider-frame::after{content:"";position:absolute;top:0;height:1px;width:50px;background:var(--gold)}
.divider-frame::before{left:0}.divider-frame::after{right:0}
.divider-word{left:0;right:0;top:88px;text-align:center;font:900 16px/1 "Roboto",sans-serif;color:var(--gold)}

/* vital functions */
.fn-box{width:78px;height:40px;border:.8px solid var(--gold);padding:9px 6px 0}
.fn-box h5{position:absolute;top:-6px;left:7px;background:var(--white);padding:0 3px;font:700 8.2px/1 "Roboto",sans-serif;color:var(--navy)}
.fn-box ol{font:400 4.4px/5.2px "Montserrat",sans-serif;color:var(--navy);padding-left:7px}
.fn-box li{margin-bottom:1.8px}

/* leadership */
.lead-num{width:19px;height:19px;background:var(--gold);display:grid;place-items:center;font:700 9px "Roboto",sans-serif;color:var(--navy)}
.lead-item h5{font:500 9.5px/1 "Roboto",sans-serif;color:var(--navy);margin-bottom:4px}
.lead-item ul{list-style:none;font:400 5.2px/8px "Montserrat",sans-serif;color:var(--text)}
.lead-item li::before{content:"▪";margin-right:4px;font-size:4px;color:var(--navy)}

/* calendar */
.cal-list{left:16px;top:55px;width:86px;font:500 5.2px/1.2 "Montserrat",sans-serif}
.cal-list dt{color:var(--gold);margin-top:4px}
.cal-list dt::before{content:"▪";margin-right:3px;font-size:4px}
.cal-list dd{color:var(--white);font:600 3.8px/5px "Montserrat",sans-serif;padding-left:6px}

/* goal badges */
.goal-card{width:53px;height:46px;background:var(--navy);color:var(--white);font:600 5.3px/6.4px "Montserrat",sans-serif;text-align:center;padding-top:23px}
.goal-dot{width:36px;height:36px;border-radius:50%;background:var(--gold);border:2px solid var(--white);display:grid;place-items:center;font:700 12px/1 "Roboto",sans-serif;color:var(--navy)}
.goal-dot small{font-size:6px}

/* production */
.prod-title{left:24px;top:54px;font:700 17.5px/19.5px "Roboto",sans-serif;color:var(--navy)}
.prod-card{width:83px;height:47px;border-radius:4px;padding:5px 8px}
.prod-card h5{font:700 8.5px/1 "Roboto",sans-serif;margin-bottom:3px}
.prod-card table{border-collapse:collapse;font:400 4.3px/7px "Montserrat",sans-serif;width:100%}
.prod-card td:first-child::before{content:"•";margin-right:3px}
.prod-card.navy{color:var(--white)}.prod-card.navy h5{color:var(--gold)}
.prod-card.gold{background:var(--gold);color:var(--white)}.prod-card.gold h5{color:var(--navy)}
.prod-note{left:218px;font:400 5.4px/8px "Montserrat",sans-serif;color:var(--navy)}
.prod-note b{font-weight:600;display:block}

/* source cards */
.src-card{width:80px;height:64px;background:var(--navy);border-radius:7px;padding:36px 6px 0 12px;font:400 3.3px/6px "Montserrat",sans-serif;color:var(--white);list-style:disc}
.src-dot{width:44px;height:44px;border-radius:50%;background:var(--gold);border:2px solid var(--white);display:grid;place-items:center;text-align:center;font:700 8.2px/1.1 "Roboto",sans-serif;color:var(--navy)}
.src-dot b{font-size:10px;display:block}

/* activity metrics */
.metric-label{font:500 6px "Montserrat",sans-serif;color:var(--navy);width:109px;text-align:center;top:39px}
.metric-box{top:48px;width:109px;height:97px;padding:5px 8px;font:400 3.1px/4.3px "Montserrat",sans-serif}
.metric-box.navy{color:var(--white)}.metric-box.gold{background:var(--gold);color:var(--navy)}
.metric-box h6{font:500 4.4px/6px "Montserrat",sans-serif;color:var(--gold)}
.metric-box.gold h6{color:var(--navy)}
.metric-box ul{padding-left:10px;margin-bottom:2px}
.metric-note{left:118px;top:149px;font:400 3.6px "Montserrat",sans-serif;color:var(--navy)}

/* bonus */
.bonus{top:62px;width:111px;height:57px;border:.8px solid var(--navy)}
.bonus h5{background:var(--navy);height:18px;display:grid;place-items:center;font:500 9.5px "Roboto",sans-serif;color:var(--gold);letter-spacing:.3px}
.bonus ul{list-style:none;padding:6px 0 0 10px;font:400 6.6px/12px "Montserrat",sans-serif;color:var(--navy)}
.bonus li::before{content:"•";margin-right:3px}

/* 36-month */
.timeline{left:0;right:0;top:69px;height:1.6px;background:var(--navy)}
.step{width:22px;height:22px;border-radius:50%;border:1.4px solid var(--navy);background:var(--white);display:grid;place-items:center;font:700 11px "Roboto",sans-serif;color:var(--navy);top:59px;box-shadow:0 0 0 1.5px var(--gold)}
.year{top:91px;width:90px;font:3.4px/4.3px "Montserrat",sans-serif;color:var(--navy)}
.year h5{font:600 7px/1 "Montserrat",sans-serif;margin-bottom:5px}
.year ul{padding-left:7px}
.year ul ul{padding-left:6px;list-style:circle}

/* servicing */
.tier{width:66px;height:93px;top:47px}
.tier .tier-name{position:absolute;left:0;right:0;top:8px;text-align:center;font:700 9px/10.5px "Roboto",sans-serif;color:var(--white)}
.tier ul{position:absolute;left:12px;top:41px;width:46px;font:600 2.9px/6px "Montserrat",sans-serif;color:var(--white);list-style:disc}

/* closing */
.thanks{left:20px;top:40px;width:130px;text-align:center;font:900 36px/43px "Roboto",sans-serif;color:var(--white);letter-spacing:-.5px}
</style>
</head>
<body>
<main class="canvas">

<!-- 1 Cover -->
<section class="slide navy" style="left:35px;top:32px">
  <svg class="photo" style="left:0;top:0" width="322" height="181" role="img" aria-label="Photo of business professionals talking in a bright office over printed financial charts">
    <defs><linearGradient id="coverPhoto" x1="0" y1="0" x2="1" y2="1"><stop offset="0" stop-color="#b9c6d4"/><stop offset=".55" stop-color="#6f7f96"/><stop offset="1" stop-color="#d4dbe6"/></linearGradient></defs>
    <polygon points="0,0 180,0 150,181 0,181" fill="url(#coverPhoto)"/>
  </svg>
  <svg style="left:0;top:0" width="322" height="181" aria-hidden="true">
    <defs><linearGradient id="coverGold" x1="0" y1="0" x2="1" y2="1"><stop offset="0" stop-color="#e6c56f"/><stop offset="1" stop-color="#9e7a2c"/></linearGradient></defs>
    <polygon points="180,0 210,0 172,110 150,181" fill="url(#coverGold)"/>
    <polygon points="195,0 210,0 172,110" fill="#c9a24a"/>
  </svg>
  <div class="sq"></div>
  <h1 class="cover-title"><span class="l1">VELTMORE</span><span class="l2">FINANCIAL</span><span class="l3">2024</span></h1>
  <div class="cover-web"><span>www.website.com</span><i></i></div>
</section>

<!-- 2 Mission -->
<section class="slide" style="left:367px;top:32px">
  <div class="side-panel"></div>
  <div class="sq left"></div>
  <h2 class="panel-head">Mission<br>Statement</h2>
  <p class="panel-copy">To provide our client with the systems and processes needed to Guide their Hero’s journey and leave an Impact</p>
  <div class="copy-block" style="top:26px">
    <h4>The Hero’s Journey :</h4>
    <p>We believe everyone has a purpose, God’s purpose in their life, and it is our mission to help our clients relentlessly pursue their purpose. A life with purpose is a life living out your Hero’s Journey!</p>
  </div>
  <div class="copy-block" style="top:71px">
    <h4>How:</h4>
    <ul>
      <li>Our financial planning &amp; wealth management services give our clients</li>
      <li>More Time &amp; Clarity on their plan and what is needed to accomplish the objective</li>
      <li>We help our clients think bigger and professionally hold them accountable to their goals</li>
      <li>We help reduce taxes drag, increase diversification, reduce investment risk, &amp; maximize investment returns so that our clients have the financial resources to maximize their potential and ultimately leave a larger Impact on the world.</li>
    </ul>
  </div>
  <div class="foot on-navy"><span>www.website.com</span><i class="rule"></i><b class="pg">2</b></div>
</section>

<!-- 3 Vision -->
<section class="slide" style="left:699px;top:32px">
  <h2 class="title" style="font-size:14px">Firm Vision<span class="vision-date">(December 2026)</span></h2>
  <div class="sq"></div>
  <ul class="fine">
    <li>We are an elite wealth management firm at Crestline Mutual that is impact driven and focused on the clients’ goals, needs, and objectives above all else. We specialize in serving executives, directors and vice presidents at leading tech firms where much of pay comes as stock.</li>
    <li>Over the last 3 years we have grown the firm organically, through introductions, and seminars and speaking events.</li>
    <li>We are the primary advisory firm and financial planning relationship for 300 households in this space. We manage over $150m in assets and our minimum account size has grown to $500k. We consistently qualify for forum and this year we will have $1M premium and $1M GDC.</li>
    <li>Our team has 3 lead advisors that are each fully responsible for servicing a sleeve of 80 – 125 clients on an annual basis. Each advisor also brings in $6M of AUM, 10 new clients and $150k of premium.</li>
    <li>Our team has a mandatory team trip every year, we don’t work weekends, we rarely work past 5pm, and every Friday the team is off by 1pm at the latest. We get in, get work done, and get out.</li>
    <li>Daniel only takes client meetings 4 days a week and no more than 16 in any given week. He has a second chair in every meeting that takes notes and handles follow up. Everyone is financially tied to the bottom line revenue. We have a team of winners!</li>
    <li>We are healthy, fit, and happy. We have the chance to help who we want when we want. We control our lives and work schedule and set the pace and cadence we want to move at.</li>
    <li>We are well on our way to managing $1B by December 2033</li>
  </ul>
  <div class="foot"><span>www.website.com</span><i class="rule"></i><b class="pg">3</b></div>
</section>

<!-- 4 Current Org -->
<section class="slide" style="left:35px;top:222px">
  <h2 class="title">Current&nbsp; Org Chart</h2><div class="bar"></div><div class="sq"></div>
  <svg style="left:0;top:0" width="322" height="181" aria-hidden="true">
    <path d="M161 86 V132 M117 132 H205" stroke="var(--navy)" stroke-width=".8" fill="none"/>
    <circle cx="161" cy="86" r="1" fill="var(--gold)"/><circle cx="117" cy="132" r="1" fill="var(--gold)"/><circle cx="205" cy="132" r="1" fill="var(--gold)"/>
    <g id="userIcon">
      <path d="M148 49 A13 13 0 0 1 174 49" stroke="var(--gold)" stroke-width="2" fill="none"/>
      <circle cx="161" cy="51" r="10" fill="#fff" stroke="var(--navy)" stroke-width="1.6"/>
      <circle cx="161" cy="51" r="6.5" fill="none" stroke="var(--navy)" stroke-width=".7"/>
      <circle cx="161" cy="49.3" r="1.8" fill="none" stroke="var(--navy)" stroke-width=".7"/>
      <path d="M157.5 55 a3.5 3 0 0 1 7 0 Z" fill="none" stroke="var(--navy)" stroke-width=".7"/>
    </g>
    <use href="#userIcon" x="-84" y="61"/>
    <use href="#userIcon" x="82" y="61"/>
  </svg>
  <div class="org-box lead" style="left:131px;top:58px">Daniel</div>
  <div class="org-box member" style="left:48px;top:119px">Mel</div>
  <div class="org-box member" style="left:214px;top:119px">Okafor</div>
  <div class="foot"><span>www.website.com</span><i class="rule"></i><b class="pg">4</b></div>
</section>

<!-- 5 Future Org -->
<section class="slide" style="left:367px;top:222px">
  <h2 class="title">Future Org Chart</h2><div class="bar"></div><div class="sq"></div>
  <svg style="left:0;top:0" width="322" height="181" aria-hidden="true">
    <path d="M160 72 V83 M83 83 H236 M83 83 V93 M130 83 V93 M186 83 V93 M236 83 V93" stroke="var(--navy)" stroke-width=".7" fill="none"/>
    <circle cx="160" cy="53" r="20" fill="#fff" stroke="var(--gold)" stroke-width="1"/>
    <circle cx="160" cy="53" r="16.5" fill="var(--navy)" role="img" aria-label="Portrait of the president"/>
    <g fill="#fff" stroke="var(--gold)" stroke-width="1">
      <circle cx="83" cy="107" r="14"/><circle cx="130" cy="107" r="14"/><circle cx="186" cy="107" r="14"/><circle cx="236" cy="107" r="14"/>
    </g>
    <g fill="#f1e3bd">
      <circle cx="83" cy="107" r="11" role="img" aria-label="Portrait of the private wealth advisor"/>
      <circle cx="130" cy="107" r="11" role="img" aria-label="Portrait of the director of insurance"/>
      <circle cx="186" cy="107" r="11" role="img" aria-label="Portrait of the director of investments"/>
      <circle cx="236" cy="107" r="11" role="img" aria-label="Portrait of the COO"/>
    </g>
  </svg>
  <p class="org-name" style="left:184px;top:48px;font-size:4.8px">DANIEL WHITFORD<span class="org-role" style="font-size:4.4px;color:var(--gold-dark)">President</span></p>
  <p class="org-name" style="left:20px;width:41px;top:101px;text-align:right">(RAVI)<span class="org-role">Private Wealth Advisor</span></p>
  <p class="org-name" style="left:105px;width:50px;top:123px;text-align:center">MELANIE<span class="org-role">Director of Insurance &amp; Office Manager</span></p>
  <p class="org-name" style="left:159px;width:54px;top:123px;text-align:center">OKAFOR<span class="org-role">Director of Investments &amp; Planning</span></p>
  <p class="org-name" style="left:254px;top:103px">OWEN HARTLEY<span class="org-role">COO</span></p>
  <div class="foot"><span>www.website.com</span><i class="rule"></i><b class="pg">5</b></div>
</section>

<!-- 6 Divider -->
<section class="slide" style="left:699px;top:222px">
  <svg class="photo" style="left:0;top:0" width="322" height="181" role="img" aria-label="Faint background photo of a rising financial bar chart in deep navy">
    <defs><radialGradient id="dividerBg" cx=".55" cy=".35" r=".8"><stop offset="0" stop-color="#1e3278"/><stop offset="1" stop-color="#07113a"/></radialGradient></defs>
    <rect width="322" height="181" fill="url(#dividerBg)"/>
  </svg>
  <h2 class="divider-text">RESPONSIBILITIES / VITAL</h2>
  <div class="divider-frame"></div>
  <p class="divider-word">FUNCTIONS</p>
</section>

<!-- 7 Vital Functions -->
<section class="slide" style="left:35px;top:414px">
  <div class="side-panel"></div>
  <div class="sq left"></div>
  <h2 class="panel-head" style="top:27px;font-size:14px">Vital<br>Functions</h2>
  <p class="panel-copy" style="top:71px;left:21px;width:70px;font-size:4.7px;line-height:6.3px">These are 3 vital functions on the leverage curve that you need to drive massive results and make it rain. Like Leon Archer say’s if we can focus on these 3 things and eliminate all other distractions we can accomplish anything!</p>
  <div class="fn-box" style="left:123px;top:38px"><h5>Daniel</h5><ol><li>Client Meeting</li><li>Dial</li><li>Business Development</li></ol></div>
  <div class="fn-box" style="left:215px;top:38px;width:89px"><h5>Okafor</h5><ol><li>Investment Processing</li><li>Final Case Prep/Executive Summary</li><li>Service Existing Book</li></ol></div>
  <div class="fn-box" style="left:123px;top:102px"><h5>Mel</h5><ol><li>Insurance Processing</li><li>Calendar Management for Daniel</li><li>OCI Manager for Daniel</li></ol></div>
  <div class="fn-box" style="left:215px;top:102px;width:89px"><h5>Owen</h5><ol><li>Activity Numbers &amp; reporting</li><li>Financials / Bookkeeping</li><li>Team Project Manger</li></ol></div>
  <div class="foot on-navy"><span>www.website.com</span><i class="rule"></i><b class="pg">7</b></div>
</section>

<!-- 8 Leadership -->
<section class="slide" style="left:367px;top:414px">
  <h2 class="title">Leadership Responsibilities</h2><div class="bar"></div><div class="sq"></div>
  <div class="lead-num" style="left:25px;top:52px">01</div>
  <div class="lead-item" style="left:49px;top:52px"><h5>Daniel</h5><ul><li>Serving A+ A Clients</li></ul></div>
  <div class="lead-num" style="left:163px;top:52px">03</div>
  <div class="lead-item" style="left:187px;top:52px"><h5>Okafor</h5><ul><li>Servicing B &amp; C Clients</li><li>New Investments account onboarding</li><li>Case Prep</li></ul></div>
  <div class="lead-num" style="left:25px;top:104px">02</div>
  <div class="lead-item" style="left:49px;top:104px"><h5>Mel</h5><ul><li>Daniels Calendar Management</li><li>Insurance Operations</li><li>Annual Reviews</li></ul></div>
  <div class="lead-num" style="left:163px;top:107px">04</div>
  <div class="lead-item" style="left:187px;top:107px"><h5>Owen</h5><ul><li>Posting and Planning</li><li>Goal Tracking</li></ul></div>
  <div class="foot"><span>www.website.com</span><i class="rule"></i><b class="pg">8</b></div>
</section>

<!-- 9 Calendar -->
<section class="slide" style="left:699px;top:414px">
  <div class="side-panel" style="width:106px"></div>
  <svg class="photo" style="left:106px;top:0" width="216" height="181" role="img" aria-label="Close-up photo of a wall calendar with coloured pins marking dates">
    <defs><linearGradient id="calPhoto" x1="0" y1="0" x2="1" y2="1"><stop offset="0" stop-color="#dfe9f7"/><stop offset=".6" stop-color="#b7cbe8"/><stop offset="1" stop-color="#eef3fa"/></linearGradient></defs>
    <rect width="216" height="181" fill="url(#calPhoto)"/>
  </svg>
  <div class="sq left"></div>
  <h2 class="panel-head" style="top:22px;font-size:11px;line-height:14px">Team Weekly<br>Calendar</h2>
  <dl class="cal-list">
    <dt>Monday :</dt><dd>▪ Team Meeting<br>▪ Daniel No meetings Monday 8-12pm</dd>
    <dt>Tuesday :</dt><dd>▪ Underwriting Emails</dd>
    <dt>Wednesday :</dt><dd>▪ Team professional development</dd>
    <dt>Thursday :</dt><dd>▪ OCI Emails</dd>
    <dt>Friday :</dt>
  </dl>
  <div class="foot on-navy"><span>www.website.com</span><i class="rule" style="visibility:hidden"></i><b class="pg">9</b></div>
</section>

<!-- 10 Awards -->
<section class="slide" style="left:35px;top:603px">
  <div class="sq left"></div>
  <h2 class="title" style="left:17px;top:22px;font-size:12px;line-height:15.5px">2024 Firm<br>Awards/Calendar<br>Year Goals</h2>
  <div class="goal-card" style="left:15px;top:95px;padding-top:27px">$1M Premium</div>
  <div class="goal-card" style="left:74px;top:95px">$18M in New AUM</div>
  <div class="goal-card" style="left:134px;top:95px">60<br>New Clients</div>
  <div class="goal-dot" style="left:23px;top:74px">$1<small>M</small></div>
  <div class="goal-dot" style="left:82px;top:74px">$18<small>M</small></div>
  <div class="goal-dot" style="left:142px;top:74px">60</div>
  <svg class="photo" style="left:193px;top:46px" width="115" height="95" role="img" aria-label="Photo of a magnifying glass over the year 2024 on a bright blue background">
    <defs><radialGradient id="awardPhoto" cx=".6" cy=".5" r=".7"><stop offset="0" stop-color="#4fc1ea"/><stop offset="1" stop-color="#1588c4"/></radialGradient></defs>
    <rect width="115" height="95" fill="url(#awardPhoto)"/>
  </svg>
  <div class="foot"><span>www.website.com</span><i class="rule"></i><b class="pg">10</b></div>
</section>

<!-- 11 Production -->
<section class="slide" style="left:367px;top:603px">
  <div class="sq" style="left:17px;top:38px"></div>
  <h2 class="prod-title">Personal<br>Production<br>Goals</h2>
  <div class="prod-card navy" style="left:124px;top:38px">
    <h5>Daniel</h5>
    <table><tr><td>Premium</td><td>: $750k</td></tr><tr><td>Net New AUM</td><td>: $12M</td></tr><tr><td>New Clients</td><td>: 48</td></tr></table>
  </div>
  <div class="prod-card gold" style="left:124px;top:92px">
    <h5>Okafor</h5>
    <table><tr><td>Premium</td><td>: $300k</td></tr><tr><td>Net New Aum</td><td>: $6M</td></tr><tr><td>New Clients</td><td>: 24</td></tr></table>
  </div>
  <p class="prod-note" style="top:52px"><b>Daniel</b>Activity goal: 20 FF / month</p>
  <p class="prod-note" style="top:105px"><b>Okafor</b>Activity goal: 15 FF / month</p>
  <div class="foot"><span>www.website.com</span><i class="rule"></i><b class="pg">11</b></div>
</section>

<!-- 12 Sources -->
<section class="slide" style="left:699px;top:603px">
  <h2 class="title">Where does it come from?</h2><div class="bar"></div><div class="sq"></div>
  <ul class="src-card" style="left:29px;top:76px"><li>New Business (Jungle): $750k</li><li>Existing Clients (Zoo): $150k</li><li>Strategic JW Partners: $100k</li></ul>
  <ul class="src-card" style="left:121px;top:76px"><li>New Business (Jungle): $10m</li><li>Existing Clients (Zoo): $ 4m</li><li>Strategic JW Partners: $ 4m</li></ul>
  <ul class="src-card" style="left:214px;top:76px"><li>Daniel: 48</li><li>Okafor: 12</li></ul>
  <div class="src-dot" style="left:45px;top:54px"><span><b>$1M</b>Premium</span></div>
  <div class="src-dot" style="left:138px;top:54px"><span><b>$18M</b>New AUM</span></div>
  <div class="src-dot" style="left:231px;top:54px"><span><b>60 New</b>Clients</span></div>
  <div class="foot"><span>www.website.com</span><i class="rule"></i><b class="pg">12</b></div>
</section>

<!-- 13 Activity -->
<section class="slide" style="left:35px;top:793px">
  <h2 class="title" style="font-size:9.5px;top:13px">Activity Metrics to make it Happen</h2><div class="bar" style="top:26px;width:28px;height:2px"></div><div class="sq"></div>
  <p class="metric-label" style="left:56px">Daniel</p>
  <p class="metric-label" style="left:167px">Okafor</p>
  <div class="metric-box navy" style="left:56px">
    <h6>• Premium</h6>
    <ul><li>240 Fact Finders in 2024</li><li>20 FF/Month</li><li>Average income/FF = $500k +</li><li>20% FF to NC ratio = 48 New Clients</li><li>4% - 5% of annual income = $22,500</li><li>Overfunded Ratio of 75% = $16,875</li><li>48 NC x $16k = $768k</li></ul>
    <h6>• AUM</h6>
    <ul><li>48 NC</li><li>50% open new Investment Account</li><li>Average Aum/household = $500k</li><li>24 x $200k = $4.8M</li></ul>
  </div>
  <div class="metric-box gold" style="left:167px">
    <h6>• Premium</h6>
    <ul><li>180 Fact Finders in 2024</li><li>16 FF/Month</li><li>Average income/FF = $250k +</li><li>12.5% FF to NC ratio = 22.5 New Clients</li><li>4% of annual income = $10,000</li><li>Overfunded Ratio of 75% = $7,500</li><li>22 NC x $7,500 = $168k</li></ul>
    <h6>• AUM</h6>
    <ul><li>22 NC</li><li>50% open new Investment Account</li><li>Average Aum/household = $250k</li><li>Assume we move less then 50%</li><li>11 x $125k = $1.375M</li></ul>
  </div>
  <p class="metric-note">•&nbsp;&nbsp; ***data would suggest we have 2x new investment account/new client.</p>
  <div class="foot"><span>www.website.com</span><i class="rule"></i><b class="pg">13</b></div>
</section>

<!-- 14 Bonus -->
<section class="slide" style="left:367px;top:793px">
  <h2 class="title">Bonus &amp; Incentive</h2><div class="sq"></div>
  <div class="bonus" style="left:38px"><h5>Forum $738k</h5><ul><li>Mel: Trip to Harbor Park</li><li>Marcus: Cash Bonus</li></ul></div>
  <div class="bonus" style="left:164px"><h5>$1M Premium</h5><ul><li>Mel: $12k Bonus</li><li>Okafor: $12k Bonus</li></ul></div>
  <div class="foot"><span>www.website.com</span><i class="rule"></i><b class="pg">14</b></div>
</section>

<!-- 15 2023 Recap -->
<section class="slide" style="left:699px;top:793px">
  <h2 class="title">2023 Recap</h2><div class="sq"></div>
  <div class="recap">
    <p>Overall, I thought it was a great year. We started the year with two key hires, but one role did not work out and we had to make a change early on. It took a lot of time and bandwidth to rebuild our meeting rhythm and protect ourselves through the hiring process while still serving clients well.</p>
    <p>In January we also saw massive layoffs in tech, which had a real impact on our market and put us behind as we were playing defense. We had over 40 prospects impacted by these layoffs, which meant more meetings, reduced premium, changed savings strategies and rolling over many plans. There was a lot of hand holding through the first 90 days of the year as the layoffs continued well into June.</p>
    <p>This also significantly impacted our front-end activity, as most of our prospects were now without a job or worried they were going to be laid off. Our current OCI pipeline, as many people were worried about more layoffs and wanted to push our planning meetings to the end of the year to make sure they were not laid off during the next wave.</p>
    <p>In June we started to work on the buyout of a retiring advisor’s book, and he officially started with us on August 1st. The first 5 months have been great. It did take several months to clean up his CRM, move over contacts, close out his current insurance business and teach him our systems and processes.</p>
    <p>We have also hired an interim COO, Owen Hartley, and I know Owen from the navy where he was a senior chief. He has been great at managing people, teams, projects, systems and processes. His brain works in a very similar way and he is detail oriented and loves the data. Owen is currently working about 8-10 hours a week as he does have another full time job.</p>
    <p>Our activity was also slightly lower this year, that is slightly because of the layoffs in tech; we were slightly undermanned in Q1 and Q2. We also leveraged joint work advisors across the region to support larger cases and grow new relationships.</p>
    <p>Overall, we are very excited for 2024 and if we can avoid any layoffs, a global pandemic, keep our team humming in the right direction and have a few joint work advisors up that can swing the bat for us, we feel very confident that we can write $1M of premium and bring over an additional $18M of net new AUM this year and hit the targets we have set.</p>
  </div>
  <div class="foot"><span>www.website.com</span><i class="rule"></i><b class="pg">15</b></div>
</section>

<!-- 16 36-month -->
<section class="slide" style="left:35px;top:986px">
  <h2 class="title">36-month Recap</h2><div class="bar"></div><div class="sq"></div>
  <div class="timeline"></div>
  <div class="step" style="left:31px">1</div>
  <div class="step" style="left:142px">2</div>
  <div class="step" style="left:248px">3</div>
  <div class="year" style="left:23px"><h5>2021: 2<sup style="font-size:4px">nd</sup> Year</h5>
    <ul><li>Premium: $686k</li><li>New Clients: 33.5</li><li>AUM: $5.3M</li><li>GDC growth: <b>455%</b><ul><li>2nd Marcus Okafor at 403%</li><li>3rd was Nate Ellis at 247%</li><li>4th Brenner at 109%</li></ul></li></ul>
    <p style="padding-left:2px">○&nbsp; West Ranking: <b>#1</b></p>
  </div>
  <div class="year" style="left:128px"><h5>2022: 3<sup style="font-size:4px">rd</sup> year</h5>
    <ul><li>Premium: $573k</li><li>New Clients: 56</li><li>Net New AUM: $5.4M</li><li>GDC growth: <b>242 %</b><ul><li>2nd closest was Peter Lang at 45%</li></ul></li><li>West Ranking: <b>#3</b></li></ul>
  </div>
  <div class="year" style="left:237px"><h5>2022: 4<sup style="font-size:4px">th</sup> year</h5>
    <ul><li>Premium: $531K</li><li>New Clients: 45</li><li>Net New AUM: $5.9M</li><li>GDC growth: <b>77%</b><ul><li>2nd Peter Lang at 56%</li><li>3rd Brenner at 53%</li></ul></li><li>West Ranking: <b>#2</b></li></ul>
  </div>
  <div class="foot"><span>www.website.com</span><i class="rule"></i><b class="pg">16</b></div>
</section>

<!-- 17 Servicing -->
<section class="slide" style="left:367px;top:986px">
  <h2 class="title">Servicing Model</h2><div class="bar"></div><div class="sq"></div>
  <svg width="0" height="0" aria-hidden="true" style="position:absolute">
    <defs>
      <linearGradient id="tGold" x1="0" y1="0" x2="1" y2="1"><stop offset="0" stop-color="#e9cb78"/><stop offset="1" stop-color="#a9822f"/></linearGradient>
      <linearGradient id="tSilver" x1="0" y1="0" x2="1" y2="1"><stop offset="0" stop-color="#f4f5f7"/><stop offset=".5" stop-color="#9ea3ab"/><stop offset="1" stop-color="#e3e5e9"/></linearGradient>
      <linearGradient id="tBronze" x1="0" y1="0" x2="1" y2="1"><stop offset="0" stop-color="#e39a59"/><stop offset="1" stop-color="#9c5224"/></linearGradient>
    </defs>
  </svg>
  <div class="tier" style="left:41px">
    <svg width="66" height="93" aria-hidden="true"><polygon points="6,2 55,0 62,30 1,36" fill="url(#tGold)"/><polygon points="3,32 63,28 63,68 6,72" fill="var(--navy)"/><polygon points="9,72 62,66 64,86 12,92" fill="url(#tGold)"/></svg>
    <p class="tier-name">Gold<br>(A/A+)</p>
    <ul><li>2 review/year</li><li>2 quarterly touchpoints</li><li>4+ hours/year</li></ul>
  </div>
  <div class="tier" style="left:129px">
    <svg width="66" height="93" aria-hidden="true"><polygon points="6,2 55,0 62,30 1,36" fill="url(#tSilver)"/><polygon points="3,32 63,28 63,68 6,72" fill="var(--navy)"/><polygon points="9,72 62,66 64,86 12,92" fill="url(#tSilver)"/></svg>
    <p class="tier-name" style="color:var(--navy)">Silver<br>(B):</p>
    <ul><li>1 annual review/year</li><li>2 quarterly touchpoints</li><li>2-4 hours/year</li></ul>
  </div>
  <div class="tier" style="left:214px">
    <svg width="66" height="93" aria-hidden="true"><polygon points="6,2 55,0 62,30 1,36" fill="url(#tBronze)"/><polygon points="3,32 63,28 63,68 6,72" fill="var(--navy)"/><polygon points="9,72 62,66 64,86 12,92" fill="url(#tBronze)"/></svg>
    <p class="tier-name">Bronze<br>(C):</p>
    <ul><li>1 annual review/year</li><li>2 quarterly touchpoints</li><li>1-2 hours/year</li></ul>
  </div>
  <div class="foot"><span>www.website.com</span><i class="rule"></i><b class="pg">17</b></div>
</section>

<!-- 18 Closing -->
<section class="slide navy" style="left:699px;top:986px">
  <svg class="photo" style="left:0;top:0" width="322" height="181" role="img" aria-label="Photo of advisors reviewing charts on a tablet and printed reports at a desk">
    <defs><linearGradient id="closePhoto" x1="0" y1="0" x2="1" y2="1"><stop offset="0" stop-color="#8a97ab"/><stop offset=".5" stop-color="#cfd6e0"/><stop offset="1" stop-color="#6d7c93"/></linearGradient></defs>
    <polygon points="200,0 322,0 322,181 152,181" fill="url(#closePhoto)"/>
  </svg>
  <svg style="left:0;top:0" width="322" height="181" aria-hidden="true">
    <defs><linearGradient id="closeGold" x1="0" y1="0" x2="1" y2="1"><stop offset="0" stop-color="#e6c56f"/><stop offset="1" stop-color="#9e7a2c"/></linearGradient></defs>
    <polygon points="188,0 206,0 158,181 130,181" fill="url(#closeGold)"/>
  </svg>
  <div class="sq left"></div><div class="sq"></div>
  <h2 class="thanks">Thank<br>You</h2>
</section>

</main>
</body>
</html>
```